Sales Flyer Design

Create a Flyer front and back that highlights the different things we do
We do Addition, basements, kitchens, bathrooms, concrete, siding, Roofing.

We want to highlight that we are licensed Electrical Contractor and Plumbers.
Use our Logo attached keeping color scheme mainly our company colors. We are looking for an attention grabbing but easy read for homeowners.

```html
<!DOCTYPE html>
<html lang="en">
<head>
<meta charset="utf-8">
<title>Northpoint Remodeling &amp; Restoration – Flyer Front and Back</title>
<link href="https://fonts.googleapis.com/css2?family=Montserrat:wght@500;600;700;800&family=Open+Sans:wght@400;600;700&display=swap" rel="stylesheet">
<style>
:root{
  --stage:#30343a;
  --blue:#2c5fa9;
  --blue-dark:#1f4784;
  --blue-deep:#183a6e;
  --orange:#e5572b;
  --orange-light:#f07a3a;
  --cream:#f3ece2;
  --cream-dark:#e6dccd;
  --white:#ffffff;
  --ink:#2a3a55;
}
*{margin:0;padding:0;box-sizing:border-box}
html,body{width:1200px;height:2836px;overflow:hidden}
body{background:var(--stage);font-family:"Open Sans",Arial,sans-serif;position:relative}
.flyer{position:absolute;left:80px;width:1040px;height:1260px;background:var(--cream);overflow:hidden;box-shadow:0 10px 30px rgba(0,0,0,.45)}
.flyer--front{top:80px}
.flyer--back{top:1488px}

.header{position:absolute;left:0;top:0;width:100%;height:240px;
  background:linear-gradient(158deg,var(--orange) 0%,var(--orange-light) 16%,var(--blue) 42%,var(--blue-dark) 100%)}
.brand{position:absolute;left:48px;top:46px;display:flex;align-items:center;gap:16px;color:var(--white);
  font-family:"Montserrat",sans-serif;font-weight:800}
.brand-mark{width:26px;height:26px;background:var(--white)}
.brand-name{font-size:34px;line-height:1.1;text-transform:uppercase;letter-spacing:1px}
.brand-name small{display:block;font-size:19px;letter-spacing:2px}
.tagline{position:absolute;right:48px;top:40px;text-align:left;color:var(--white);
  font-family:"Montserrat",sans-serif;font-weight:600;font-size:46px;line-height:1.18}
.tagline strong{color:var(--orange-light);font-weight:800}
.swoosh{position:absolute;right:40px;top:176px}

.licensed{position:absolute;left:0;width:100%;height:56px;background:var(--white);
  display:flex;align-items:center;justify-content:center;
  font-family:"Montserrat",sans-serif;font-weight:700;font-size:25px;color:var(--blue);letter-spacing:.5px}
.flyer--front .licensed{top:296px}
.flyer--back .licensed{top:244px}

.photo-band{position:absolute;left:0;top:352px;width:100%;height:420px;
  background:linear-gradient(180deg,var(--blue) 0%,var(--blue-dark) 70%,var(--cream) 100%)}
.photo{position:absolute;top:392px;width:296px;height:360px;border:8px solid var(--white);box-shadow:0 6px 14px rgba(0,0,0,.3)}
.photo--living{left:56px;background:linear-gradient(180deg,#cfc3b2,#8c7a66)}
.photo--bedroom{left:372px;background:linear-gradient(180deg,#e0d6c7,#a7917a)}
.photo--bath{left:688px;background:linear-gradient(180deg,#d9d9d6,#8f8f8c)}

.section-title{position:absolute;left:0;width:100%;text-align:center;
  font-family:"Montserrat",sans-serif;font-weight:800;font-size:30px;color:var(--blue)}
.flyer--front .section-title{top:790px}

.services{position:absolute;left:90px;top:852px;width:880px;display:grid;grid-template-columns:1fr 1fr;row-gap:22px;column-gap:60px}
.service{display:flex;align-items:center;gap:18px}
.service-icon{width:56px;height:56px;background:var(--orange);border-radius:6px;display:flex;align-items:center;justify-content:center;flex:none}
.service h3{font-family:"Montserrat",sans-serif;font-weight:800;font-size:28px;color:var(--blue);line-height:1.05}
.service p{font-size:17px;color:var(--ink)}

.promise-bar{position:absolute;left:0;top:1106px;width:100%;height:52px;background:var(--blue-dark);
  display:flex;align-items:center;justify-content:center;gap:26px;color:var(--white);
  font-family:"Montserrat",sans-serif;font-weight:600;font-size:20px}
.promise-bar span{display:flex;align-items:center;gap:8px}
.promise-bar .divider{width:2px;height:22px;background:rgba(255,255,255,.6)}

.footer{position:absolute;left:0;bottom:0;width:100%;height:100px;
  background:linear-gradient(90deg,var(--orange) 0%,var(--orange-light) 100%);
  display:flex;align-items:center;padding:0 30px;color:var(--white)}
.footer-address{display:flex;align-items:center;gap:10px;font-size:15px;line-height:1.3;width:330px}
.footer-cta{flex:1;text-align:center;font-family:"Montserrat",sans-serif;font-weight:700;font-size:22px}
.footer-phone{display:flex;align-items:center;gap:10px;background:var(--blue);border-radius:30px;padding:10px 26px;
  font-family:"Montserrat",sans-serif;font-weight:800;font-size:32px}
.flyer--back .footer{height:64px}
.flyer--back .footer-phone{font-size:30px;padding:6px 24px}

.services-band{position:absolute;left:0;top:300px;width:100%;height:230px;
  background:linear-gradient(180deg,var(--blue) 0%,var(--blue-dark) 100%);
  padding-top:34px;text-align:center;color:var(--white);
  font-family:"Montserrat",sans-serif;font-weight:700;font-size:19px;line-height:2.05;letter-spacing:.3px}
.services-band .sep{color:var(--orange-light);margin:0 8px}

.why-band{position:absolute;left:0;top:530px;width:100%;height:54px;background:var(--orange);
  display:flex;align-items:center;justify-content:center;color:var(--white);
  font-family:"Montserrat",sans-serif;font-weight:800;font-size:26px}
.reasons{position:absolute;left:40px;top:600px;width:960px;display:grid;grid-template-columns:repeat(3,1fr);gap:30px;text-align:center}
.reason svg{display:block;margin:0 auto 8px}
.reason h3{font-family:"Montserrat",sans-serif;font-weight:800;font-size:22px;color:var(--orange)}
.reason p{font-size:16px;color:var(--ink);line-height:1.35;margin-top:4px;padding:0 20px}

.photo-patio{position:absolute;left:0;top:790px;width:100%;height:360px;
  background:linear-gradient(180deg,#b9cbd8 0%,#7f9a6e 40%,#c9b9a3 75%,#8d8175 100%)}
.closing-bar{position:absolute;left:0;top:1150px;width:100%;height:46px;background:var(--blue-dark);
  display:flex;align-items:center;justify-content:center;gap:10px;color:var(--white);
  font-family:"Montserrat",sans-serif;font-weight:700;font-size:20px}
</style>
</head>
<body>

<!-- FRONT -->
<section class="flyer flyer--front">
  <header class="header">
    <div class="brand"><span class="brand-mark"></span><div class="brand-name">Northpoint<small>Remodeling &amp; Restoration</small></div></div>
    <h1 class="tagline">Transform Your Home<br>with <strong>CONFIDENCE!</strong></h1>
    <svg class="swoosh" width="460" height="30" viewBox="0 0 460 30"><path d="M0 26 Q230 -6 460 14" stroke="#fff" stroke-width="5" fill="none"/></svg>
  </header>
  <div class="licensed">LICENSED ELECTRICAL CONTRACTOR AND PLUMBERS</div>
  <div class="photo-band"></div>
  <div class="photo photo--living" role="img" aria-label="Photo of a bright renovated living room"></div>
  <div class="photo photo--bedroom" role="img" aria-label="Photo of a cozy finished bedroom"></div>
  <div class="photo photo--bath" role="img" aria-label="Photo of a modern walk-in shower bathroom"></div>

  <h2 class="section-title">FROM CONCEPT TO COMPLETION – WE DO IT ALL:</h2>
  <div class="services">
    <div class="service"><div class="service-icon"><svg width="34" height="34" viewBox="0 0 34 34" fill="none" stroke="#fff" stroke-width="3"><path d="M4 17 L17 5 L30 17 M8 14 V29 H26 V14"/><path d="M17 18 V26 M13 22 H21"/></svg></div><div><h3>ADDITIONS</h3><p>Expand your living space beautifully</p></div></div>
    <div class="service"><div class="service-icon"><svg width="34" height="34" viewBox="0 0 34 34" fill="none" stroke="#fff" stroke-width="3"><path d="M4 15 L17 5 L30 15 V29 H4 Z"/><path d="M4 22 H30"/></svg></div><div><h3>BASEMENTS</h3><p>Finished spaces that add value</p></div></div>
    <div class="service"><div class="service-icon"><svg width="34" height="34" viewBox="0 0 34 34" fill="none" stroke="#fff" stroke-width="3"><rect x="5" y="12" width="24" height="17"/><path d="M5 18 H29 M17 12 V29 M10 5 V9 M24 5 V9"/></svg></div><div><h3>KITCHENS</h3><p>Custom designs for how you live</p></div></div>
    <div class="service"><div class="service-icon"><svg width="34" height="34" viewBox="0 0 34 34" fill="none" stroke="#fff" stroke-width="3"><path d="M4 17 H30 V21 A8 8 0 0 1 22 29 H12 A8 8 0 0 1 4 21 Z M8 17 V7 A3 3 0 0 1 14 7"/></svg></div><div><h3>BATHROOMS</h3><p>From basic to spa-like luxury</p></div></div>
    <div class="service"><div class="service-icon"><svg width="34" height="34" viewBox="0 0 34 34" fill="none" stroke="#fff" stroke-width="3"><rect x="4" y="6" width="26" height="22"/><path d="M4 17 H30 M13 6 V17 M21 17 V28"/></svg></div><div><h3>CONCRETE WORK</h3><p>Patios, driveways, walkways &amp; more</p></div></div>
    <div class="service"><div class="service-icon"><svg width="34" height="34" viewBox="0 0 34 34" fill="none" stroke="#fff" stroke-width="3"><path d="M3 16 L17 5 L31 16 M7 13 V29 H27 V13 M7 19 H27 M7 24 H27"/></svg></div><div><h3>SIDING &amp; ROOFING</h3><p>Protection that looks great too</p></div></div>
  </div>

  <div class="promise-bar">
    <span><svg width="20" height="20" viewBox="0 0 20 20"><path d="M3 10 L8 15 L17 4" stroke="#fff" stroke-width="3" fill="none"/></svg>Quality Workmanship</span><i class="divider"></i>
    <span><svg width="20" height="20" viewBox="0 0 20 20"><path d="M3 10 L8 15 L17 4" stroke="#fff" stroke-width="3" fill="none"/></svg>Honest Pricing</span><i class="divider"></i>
    <span><svg width="20" height="20" viewBox="0 0 20 20"><path d="M3 10 L8 15 L17 4" stroke="#fff" stroke-width="3" fill="none"/></svg>Projects Done Right — The First Time</span>
  </div>

  <footer class="footer">
    <div class="footer-address"><svg width="22" height="28" viewBox="0 0 22 28"><path d="M11 1 A10 10 0 0 1 21 11 C21 18 11 27 11 27 C11 27 1 18 1 11 A10 10 0 0 1 11 1 Z" fill="#fff"/><circle cx="11" cy="11" r="4" fill="#e5572b"/></svg><span>218 Maple Crest Drive,<br>Suite 12 Westfield, IA 50999</span></div>
    <div class="footer-cta">CALL FOR FREE ESTIMATE</div>
    <div class="footer-phone"><svg width="26" height="26" viewBox="0 0 24 24"><path d="M6.6 10.8a15 15 0 0 0 6.6 6.6l2.2-2.2a1 1 0 0 1 1-.25 11.4 11.4 0 0 0 3.6.57 1 1 0 0 1 1 1V20a1 1 0 0 1-1 1A17 17 0 0 1 3 4a1 1 0 0 1 1-1h3.5a1 1 0 0 1 1 1c0 1.25.2 2.45.57 3.57a1 1 0 0 1-.25 1z" fill="#fff"/></svg>(555) 014-2790</div>
  </footer>
</section>

<!-- BACK -->
<section class="flyer flyer--back">
  <header class="header" style="height:232px">
    <div class="brand"><span class="brand-mark"></span><div class="brand-name">Northpoint<small>Remodeling &amp; Restoration</small></div></div>
    <h1 class="tagline">Transform Your Home<br>with <strong>CONFIDENCE!</strong></h1>
    <svg class="swoosh" width="460" height="30" viewBox="0 0 460 30"><path d="M0 26 Q230 -6 460 14" stroke="#fff" stroke-width="5" fill="none"/></svg>
  </header>
  <div class="licensed">LICENSED ELECTRICAL CONTRACTOR AND PLUMBERS</div>

  <div class="services-band">
    BATHROOM MAKEOVERS<span class="sep">|</span>MODERN KITCHEN RENOVATIONS<span class="sep">|</span>BASEMENT FINISHING<br>
    ADDITIONS &amp; EXPANSIONS<span class="sep">|</span>NEW SIDING &amp; ROOFING INSTALLATION<span class="sep">|</span>ELECTRICAL UPGRADES<br>
    PLUMBING INSTALLATIONS &amp; REPAIRS<span class="sep">|</span>CONCRETE WORK &amp; DRIVEWAYS
  </div>

  <div class="why-band">WHY CHOOSE US? BECAUSE YOUR HOME DESERVES THE BEST.</div>
  <div class="reasons">
    <div class="reason"><svg width="52" height="52" viewBox="0 0 52 52" fill="none" stroke="#2c5fa9" stroke-width="3"><circle cx="26" cy="18" r="10"/><path d="M20 27 L16 46 L26 40 L36 46 L32 27"/></svg><h3>EXPERT CRAFTSMANSHIP</h3><p>We bring years of hands-on experience to every job.</p></div>
    <div class="reason"><svg width="52" height="52" viewBox="0 0 52 52" fill="none" stroke="#2c5fa9" stroke-width="3"><circle cx="26" cy="14" r="7"/><path d="M12 44 V34 A14 14 0 0 1 40 34 V44"/><circle cx="9" cy="22" r="4"/><circle cx="43" cy="22" r="4"/></svg><h3>ALL-IN-ONE SERVICE</h3><p>No need to hire multiple contractors - we do it all, and we do it right.</p></div>
    <div class="reason"><svg width="52" height="52" viewBox="0 0 52 52" fill="none" stroke="#2c5fa9" stroke-width="3"><rect x="6" y="10" width="40" height="32" rx="3"/><circle cx="19" cy="23" r="5"/><path d="M11 35 A8 8 0 0 1 27 35 M31 20 H41 M31 27 H41"/></svg><h3>LICENSED &amp; INSURED</h3><p>Rest easy knowing you're working with qualified professionals.</p></div>
  </div>

  <div class="photo-patio" role="img" aria-label="Photo of an outdoor patio with sofas and a fire table surrounded by greenery"></div>

  <div class="closing-bar">
    <svg width="20" height="20" viewBox="0 0 20 20"><path d="M3 10 L8 15 L17 4" stroke="#fff" stroke-width="3" fill="none"/></svg>Local
    <svg width="20" height="20" viewBox="0 0 20 20"><path d="M3 10 L8 15 L17 4" stroke="#fff" stroke-width="3" fill="none"/></svg>Reliable
    <svg width="20" height="20" viewBox="0 0 20 20"><path d="M3 10 L8 15 L17 4" stroke="#fff" stroke-width="3" fill="none"/></svg>Professional - Let's make your dream home a reality.
  </div>

  <footer class="footer">
    <div class="footer-address"><svg width="22" height="28" viewBox="0 0 22 28"><path d="M11 1 A10 10 0 0 1 21 11 C21 18 11 27 11 27 C11 27 1 18 1 11 A10 10 0 0 1 11 1 Z" fill="#fff"/><circle cx="11" cy="11" r="4" fill="#e5572b"/></svg><span>218 Maple Crest Drive,<br>Suite 12 Westfield, IA 50999</span></div>
    <div class="footer-cta">CALL FOR FREE ESTIMATE</div>
    <div class="footer-phone"><svg width="24" height="24" viewBox="0 0 24 24"><path d="M6.6 10.8a15 15 0 0 0 6.6 6.6l2.2-2.2a1 1 0 0 1 1-.25 11.4 11.4 0 0 0 3.6.57 1 1 0 0 1 1 1V20a1 1 0 0 1-1 1A17 17 0 0 1 3 4a1 1 0 0 1 1-1h3.5a1 1 0 0 1 1 1c0 1.25.2 2.45.57 3.57a1 1 0 0 1-.25 1z" fill="#fff"/></svg>(555) 014-2790</div>
  </footer>
</section>

</body>
</html>
```